Business Card Design

redesign of card and recreation of logo based on image provided. the business is located in new york so the Harwell Viaduct figures prominently in the scheme. product should be very clean.

Industry/Entity Type

Real Estate

Contact Information for Business Card

Otto Kilbane 318 Tamsett Avenue Marlow Park, New York 10997 otto@kelmrq.com Mobile: 555-014-7293

Colors
cadf82
1b1b1b
ffffff

Requirements
Nice to have
• Harwell Viaduct

```html
<!DOCTYPE html>
<html lang="en">
<head>
<meta charset="utf-8">
<title>Kilbane Realty Group — Business Card</title>
<link href="https://fonts.googleapis.com/css2?family=Open+Sans:wght@400;600;700&display=swap" rel="stylesheet">
<style>
  :root {
    --olive: #cadf82;
    --ink: #1b1b1b;
    --paper: #ffffff;
    --backdrop: #e9e7e3;
    --muted: #bdbdbd;
  }
  html, body {
    margin: 0;
    width: 1200px;
    height: 913px;
    overflow: hidden;
    background: var(--backdrop);
    font-family: "Open Sans", Arial, sans-serif;
  }
  .sheet {
    width: 1200px;
    height: 913px;
    display: flex;
    align-items: center;
    justify-content: center;
    gap: 50px;
  }
  .card {
    position: relative;
    width: 530px;
    height: 303px;
    border-radius: 16px;
    overflow: hidden;
    box-shadow: 0 8px 24px rgba(0,0,0,.18);
  }
  .card--front { background: var(--ink); color: var(--paper); }
  .card--back { background: var(--paper); color: var(--ink); }

  .viaduct { position: absolute; border-radius: 4px; }
  .card--front .viaduct {
    right: 40px; top: 22px; width: 260px; height: 76px;
    background: linear-gradient(90deg, #4a4a4a, #8a8a8a);
  }
  .card--back .viaduct {
    left: 50%; top: 48px; width: 300px; height: 130px;
    transform: translateX(-50%);
    background: linear-gradient(90deg, #2e2e2e, #9a9a9a);
  }

  .wordmark {
    position: absolute;
    font-weight: 600;
    white-space: nowrap;
  }
  .card--front .wordmark { right: 40px; top: 104px; font-size: 20px; color: var(--paper); }
  .card--back .wordmark { left: 0; right: 0; top: 196px; text-align: center; font-size: 30px; color: var(--ink); }

  .divider {
    position: absolute;
    left: 34px; right: 34px; top: 142px;
    height: 1px;
    background: var(--muted);
  }
  .address {
    position: absolute;
    right: 40px; top: 154px;
    text-align: right;
    font-size: 13px;
    font-weight: 600;
    line-height: 1.45;
  }
  .identity {
    position: absolute;
    left: 0; top: 170px;
    display: flex;
  }
  .identity__tab { width: 22px; height: 40px; background: var(--paper); border-right: 5px solid var(--olive); }
  .identity__text { padding-left: 12px; }
  .identity__name { font-size: 21px; font-weight: 700; line-height: 1.05; text-transform: uppercase; }
  .identity__role { font-size: 13px; font-weight: 600; color: var(--olive); letter-spacing: .5px; }

  .contacts {
    position: absolute;
    left: 39px; top: 218px;
    margin: 0; padding: 0;
    list-style: none;
    font-size: 13px;
    line-height: 17px;
  }
  .contacts li { display: flex; align-items: center; gap: 8px; }
  .contacts svg { width: 11px; height: 11px; fill: none; stroke: var(--olive); stroke-width: 1.6; }
</style>
</head>
<body>
<main class="sheet">

  <section class="card card--front" aria-label="Card front">
    <div class="viaduct" role="img" aria-label="Line illustration of the Harwell Viaduct"></div>
    <div class="wordmark">Kilbane Realty Group</div>
    <div class="divider"></div>
    <div class="address">318 Tamsett Avenue<br>Marlow Park, New York 10997</div>
    <div class="identity">
      <div class="identity__tab"></div>
      <div class="identity__text">
        <div class="identity__name">Otto Kilbane</div>
        <div class="identity__role">BROKER</div>
      </div>
    </div>
    <ul class="contacts">
      <li><svg viewBox="0 0 12 12"><path d="M2 1l2 0 1 3-1.5 1a6 6 0 0 0 3.5 3.5L8 7l3 1v2a1 1 0 0 1-1 1A9 9 0 0 1 1 2a1 1 0 0 1 1-1z"/></svg>555-014-7293</li>
      <li><svg viewBox="0 0 12 12"><rect x="3" y="1" width="6" height="10" rx="1"/><path d="M5 9h2"/></svg>555-014-0000</li>
      <li><svg viewBox="0 0 12 12"><rect x="1" y="2.5" width="10" height="7"/><path d="M1 2.5l5 4 5-4"/></svg>otto@kelmrq.com</li>
      <li><svg viewBox="0 0 12 12"><circle cx="6" cy="6" r="5"/><path d="M1 6h10M6 1c-2.5 3-2.5 7 0 10M6 1c2.5 3 2.5 7 0 10"/></svg>www.kelmrqnyc.com</li>
    </ul>
  </section>

  <section class="card card--back" aria-label="Card back">
    <div class="viaduct" role="img" aria-label="Large line illustration of the Harwell Viaduct"></div>
    <div class="wordmark">Kilbane Realty Group</div>
  </section>

</main>
</body>
</html>
```